Tradeshow Banner Design (Qty2, 6'H x 2'W)

Brightwell Contractors is an Electrical, Fire Alarm, and Security Contracting company. For tradeshows, we would like 2 vertical Banners to put behind our booth. Our colors are Red, Grey & Black. I would like the Banners to be informative on what services we provide, with some appealing Graphic Design. (bwc-kmo.com)
Slogan: Safeguarding Communities Electrical, Fire & Security Solutions
Target Market(s)
Commercial Construction Clients
Industry/Entity Type
Electrical / Construction
Font styles to use
Other font styles liked:
- Aileron
Colors
EB3D1F
EC4F4E
F09395
F8D3D4
FCEDEE
Requirements
Must have
- Our Logo, Color Scheme, Brief Caption of the services we provide
Nice to have
- Appealing Imagery & a modern/simplistic design

```html
<!DOCTYPE html>
<html lang="en">
<head>
<meta charset="utf-8">
<title>Brightwell Contractors – Tradeshow Banners</title>
<link rel="stylesheet" href="https://fonts.googleapis.com/css2?family=Montserrat:wght@400;500;600;700&family=Raleway:wght@400;500&display=swap">
<style>
  :root{
    --stage:#6d6d6f;
    --red:#ec2227;
    --black:#050608;
    --grey:#58595c;
    --grey-ring:#6a6b6e;
    --white:#ffffff;
    --ink:#2b2b2b;
  }
  *{box-sizing:border-box;margin:0;padding:0}
  html,body{width:1067px;height:1200px;overflow:hidden;background:var(--stage)}
  body{position:relative;font-family:"Montserrat",Arial,sans-serif}
  .banner{position:absolute;top:39px;width:374px;height:1122px;background:var(--white);overflow:hidden;box-shadow:0 6px 18px rgba(0,0,0,.25)}
  .banner--left{left:139px}
  .banner--right{left:593px}

  .hero{position:absolute;left:0;top:0;width:100%;height:405px;background:var(--black)}
  .hero__photo{position:absolute;left:0;top:60px;width:100%;height:300px;
    background:linear-gradient(180deg,#2e3036 0%,#3b3a38 45%,#1b1c1f 78%,var(--black) 100%)}
  .hero__wave{position:absolute;left:0;top:0;width:100%;height:140px}
  .brand{position:absolute;left:43px;top:22px;display:flex;align-items:center;gap:8px}
  .brand__mark{width:60px;height:60px;border-radius:50%;background:var(--white)}
  .brand__text{color:var(--white)}
  .brand__name{font-weight:700;font-size:17px;line-height:1.05;letter-spacing:.3px;text-transform:uppercase;width:110px}
  .brand__tag{font-size:6.5px;font-weight:500;letter-spacing:.4px;margin-top:3px}
  .hero__title{position:absolute;left:0;top:322px;width:100%;text-align:center;color:var(--white);
    font-weight:600;font-size:22px;line-height:31px;letter-spacing:1px;white-space:nowrap}

  .intro{position:absolute;left:43px;top:445px;width:287px}
  .intro__head{height:51px;background:var(--red);border-radius:4px;color:var(--white);text-align:center;
    font-weight:600;font-size:15.5px;line-height:19px;padding-top:6px;box-shadow:0 2px 2px rgba(0,0,0,.3)}
  .intro__body{height:85px;background:var(--white);box-shadow:0 1px 4px rgba(0,0,0,.25);
    font-family:"Raleway",Arial,sans-serif;font-size:7.2px;line-height:11px;color:var(--ink);
    text-align:justify;text-align-last:center;padding:18px 20px 0}

  .services__head{position:absolute;left:43px;top:612px;width:287px;height:31px;background:var(--grey);
    border-radius:4px;color:var(--white);text-align:center;font-weight:500;font-size:15px;line-height:31px;
    box-shadow:0 2px 2px rgba(0,0,0,.35)}
  .service-label{position:absolute;width:132px;height:31px}
  .service-label__bar{position:absolute;left:20px;top:5px;right:0;height:22px;background:var(--red);
    color:var(--white);font-weight:600;font-size:10.5px;line-height:22px;padding-left:14px;white-space:nowrap;overflow:hidden}
  .service-label__bar--long{font-size:9px;padding-left:13px}
  .service-label__icon{position:absolute;left:0;top:0;width:31px;height:31px;border-radius:50%;
    background:var(--white);border:2.5px solid var(--grey-ring);display:flex;align-items:center;justify-content:center}
  .service-label__icon svg{width:17px;height:17px}
  .service-photo{position:absolute;width:132px;height:84px;border-radius:5px}
  .photo--fire{background:linear-gradient(120deg,#e9e7e4 0%,#d6d4d2 30%,#c8221f 55%,#9b1512 100%)}
  .photo--keypad{background:linear-gradient(120deg,#1e1e24 0%,#6c6877 45%,#9a97a8 60%,#2a2a30 100%)}
  .photo--camera{background:linear-gradient(180deg,#474a50 0%,#5e6168 50%,#3d4046 100%)}
  .photo--panel{background:linear-gradient(120deg,#8a7a60 0%,#3d3b3a 40%,#c26b2a 60%,#2d2f35 100%)}

  .col-a{left:43px}
  .col-b{left:197px}

  .contact{position:absolute;left:0;top:973px;width:100%;height:149px;background:var(--black);color:var(--white)}
  .contact__inner{position:absolute;left:153px;top:36px;width:177px}
  .contact__title{font-weight:500;font-size:15px;padding-bottom:3px;border-bottom:1px solid #6d6d6d}
  .contact__phone{font-weight:500;font-size:13px;margin-top:6px;letter-spacing:.6px}
  .contact__email{font-size:8.5px;font-weight:500;margin-top:6px}
  .contact__address{font-size:8px;font-weight:600;margin-top:8px;line-height:11px;letter-spacing:.2px}
</style>
</head>
<body>

<section class="banner banner--left">
  <header class="hero">
    <div class="hero__photo" role="img" aria-label="Modern commercial office building at dusk"></div>
    <svg class="hero__wave" viewBox="0 0 374 140" preserveAspectRatio="none" aria-hidden="true">
      <path d="M0,0 H374 V92 C366,80 356,74 340,74 C300,76 230,110 150,124 C90,134 40,128 0,106 Z" fill="#ffffff"/>
      <path d="M0,0 H374 V86 C366,74 355,68 340,68 C300,70 230,104 150,118 C90,128 40,122 0,100 Z" fill="var(--red)"/>
    </svg>
    <div class="brand">
      <div class="brand__mark"></div>
      <div class="brand__text">
        <div class="brand__name">Brightwell Contractors</div>
        <div class="brand__tag">ELECTRICAL | FIRE | SECURITY</div>
      </div>
    </div>
    <h1 class="hero__title">COMMERCIAL&nbsp; PROPERTY<br>PROTECTION</h1>
  </header>

  <div class="intro">
    <h2 class="intro__head">We help our clients get<br>peace of mind</h2>
    <p class="intro__body">As a family business, we have laid a grounded and honest foundation while taking pride in our employees and our work. At Brightwell Contractors, our customers choose to do business with us because we are dedicated and loyal. Our work is not over when we leave the job site or lock up at the office.</p>
  </div>

  <h2 class="services__head">our Services</h2>

  <div class="service-label col-a" style="top:668px">
    <div class="service-label__bar">Fire protection</div>
    <div class="service-label__icon"><svg viewBox="0 0 24 24"><path d="M12 3c1 4 5 6 5 11a5 5 0 0 1-10 0c0-3 2-4 2-7 2 1 3 3 3 5" fill="none" stroke="#555" stroke-width="1.8"/></svg></div>
  </div>
  <div class="service-label col-b" style="top:668px">
    <div class="service-label__bar">Security</div>
    <div class="service-label__icon"><svg viewBox="0 0 24 24"><path d="M12 3l7 3v5c0 5-3 8-7 10-4-2-7-5-7-10V6z" fill="none" stroke="#555" stroke-width="1.8"/></svg></div>
  </div>
  <div class="service-photo photo--fire col-a" style="top:702px" role="img" aria-label="Hand pressing a red fire alarm call point"></div>
  <div class="service-photo photo--keypad col-b" style="top:702px" role="img" aria-label="Security keypad mounted on a wall"></div>
  <div class="service-photo photo--camera col-a" style="top:806px" role="img" aria-label="Two surveillance cameras on a grey wall"></div>
  <div class="service-photo photo--panel col-b" style="top:806px" role="img" aria-label="Electrician testing an electrical panel with a meter"></div>
  <div class="service-label col-a" style="top:906px">
    <div class="service-label__bar">Surveillance</div>
    <div class="service-label__icon"><svg viewBox="0 0 24 24"><path d="M4 7h12l2 5H6zM9 12v5H5M18 9l3 1" fill="none" stroke="#555" stroke-width="1.8"/></svg></div>
  </div>
  <div class="service-label col-b" style="top:906px">
    <div class="service-label__bar service-label__bar--long">Electrical services</div>
    <div class="service-label__icon"><svg viewBox="0 0 24 24"><circle cx="12" cy="12" r="8" fill="none" stroke="#555" stroke-width="1.6"/><path d="M13 6l-4 7h3l-1 5 4-7h-3z" fill="#555"/></svg></div>
  </div>

  <footer class="contact">
    <div class="contact__inner">
      <h3 class="contact__title">Contact us</h3>
      <p class="contact__phone">253-555-0148</p>
      <p class="contact__email">office@bwc-kmo.com</p>
      <p class="contact__address">2210 Harbor Ridge Way STE 310<br>Kent, WA 98031</p>
    </div>
  </footer>
</section>

<section class="banner banner--right">
  <header class="hero">
    <div class="hero__photo" role="img" aria-label="Modern commercial office building at dusk"></div>
    <svg class="hero__wave" viewBox="0 0 374 140" preserveAspectRatio="none" aria-hidden="true">
      <path d="M0,0 H374 V92 C366,80 356,74 340,74 C300,76 230,110 150,124 C90,134 40,128 0,106 Z" fill="#ffffff"/>
      <path d="M0,0 H374 V86 C366,74 355,68 340,68 C300,70 230,104 150,118 C90,128 40,122 0,100 Z" fill="var(--red)"/>
    </svg>
    <div class="brand">
      <div class="brand__mark"></div>
      <div class="brand__text">
        <div class="brand__name">Brightwell Contractors</div>
        <div class="brand__tag">ELECTRICAL | FIRE | SECURITY</div>
      </div>
    </div>
    <h1 class="hero__title">COMMERCIAL&nbsp; PROPERTY<br>PROTECTION</h1>
  </header>

  <div class="intro">
    <h2 class="intro__head">We help our clients get<br>peace of mind</h2>
    <p class="intro__body">As a family business, we have laid a grounded and honest foundation while taking pride in our employees and our work. At Brightwell Contractors, our customers choose to do business with us because we are dedicated and loyal. Our work is not over when we leave the job site or lock up at the office.</p>
  </div>

  <h2 class="services__head">our Services</h2>

  <div class="service-label col-a" style="top:668px">
    <div class="service-label__bar">Fire protection</div>
    <div class="service-label__icon"><svg viewBox="0 0 24 24"><path d="M12 3c1 4 5 6 5 11a5 5 0 0 1-10 0c0-3 2-4 2-7 2 1 3 3 3 5" fill="none" stroke="#555" stroke-width="1.8"/></svg></div>
  </div>
  <div class="service-label col-b" style="top:668px">
    <div class="service-label__bar">Security</div>
    <div class="service-label__icon"><svg viewBox="0 0 24 24"><path d="M12 3l7 3v5c0 5-3 8-7 10-4-2-7-5-7-10V6z" fill="none" stroke="#555" stroke-width="1.8"/></svg></div>
  </div>
  <div class="service-photo photo--fire col-a" style="top:702px" role="img" aria-label="Hand pressing a red fire alarm call point"></div>
  <div class="service-photo photo--keypad col-b" style="top:702px" role="img" aria-label="Security keypad mounted on a wall"></div>
  <div class="service-photo photo--camera col-a" style="top:806px" role="img" aria-label="Two surveillance cameras on a grey wall"></div>
  <div class="service-photo photo--panel col-b" style="top:806px" role="img" aria-label="Electrician testing an electrical panel with a meter"></div>
  <div class="service-label col-a" style="top:906px">
    <div class="service-label__bar">Surveillance</div>
    <div class="service-label__icon"><svg viewBox="0 0 24 24"><path d="M4 7h12l2 5H6zM9 12v5H5M18 9l3 1" fill="none" stroke="#555" stroke-width="1.8"/></svg></div>
  </div>
  <div class="service-label col-b" style="top:906px">
    <div class="service-label__bar service-label__bar--long">Electrical services</div>
    <div class="service-label__icon"><svg viewBox="0 0 24 24"><circle cx="12" cy="12" r="8" fill="none" stroke="#555" stroke-width="1.6"/><path d="M13 6l-4 7h3l-1 5 4-7h-3z" fill="#555"/></svg></div>
  </div>

  <footer class="contact">
    <div class="contact__inner">
      <h3 class="contact__title">Contact us</h3>
      <p class="contact__phone">253-555-0148</p>
      <p class="contact__email">office@bwc-kmo.com</p>
      <p class="contact__address">2210 Harbor Ridge Way STE 310<br>Kent, WA 98031</p>
    </div>
  </footer>
</section>

</body>
</html>
```